Feld und Klang
Zielgruppe
GPS Audio Apps, Entwicklung von Audio-Guides für Draußen
potentielle Auftraggeber: Standortmarketing, Tourismusmarketing, Gemeinden, Kulturinstitutionen
Aufgabenstellung
Layout Briefkopf /Visitenkarte
Text:
Feld und Klang (Feld und Klang)
GPS AUDIO APPS
www.feld-und-klang-beispiel.de
Visitenkarte Rückseite: Orte zum Sprechen bringen...
Das PDF zeigt einen ersten Versuch meinerseits, ich bin aber auch für ganz andere Vorschläge offen. Generell stelle ich mir eine schlichte Typographie vor, ohne Icons oder Ähnliches.

```html
<!DOCTYPE html>
<html lang="de">
<head>
<meta charset="utf-8">
<title>Feld und Klang – Visitenkarten</title>
<link rel="stylesheet" href="https://fonts.googleapis.com/css2?family=Source+Sans+3:wght@400;700&family=Exo+2:ital,wght@0,600;1,300&display=swap">
<style>
  :root {
    --brand-red: #c1262f;
    --text-grey: #58595b;
    --page-bg: #f7f7f7;
    --card-white: #ffffff;
  }
  * { margin: 0; padding: 0; box-sizing: border-box; }
  html, body { width: 1200px; height: 1200px; overflow: hidden; background: var(--page-bg); }
  body { position: relative; font-family: "Source Sans 3", sans-serif; color: var(--text-grey); }

  .card {
    position: absolute;
    width: 487px;
    height: 291px;
    overflow: hidden;
    box-shadow: 6px 6px 6px rgba(0,0,0,0.55);
  }
  .card--front { background: var(--card-white); }
  .card--back { background: var(--brand-red); }

  .card--row1 { top: 176px; }
  .card--row2 { top: 635px; }
  .card--left { left: 80px; }
  .card--right { left: 651px; }

  .brand-name {
    position: absolute;
    left: 32px;
    top: 27px;
    font-weight: 700;
    font-size: 42px;
    line-height: 1;
    color: var(--text-grey);
    white-space: nowrap;
  }
  .brand-tagline {
    position: absolute;
    left: 33px;
    top: 75px;
    font-weight: 400;
    font-size: 31px;
    line-height: 1;
    letter-spacing: 4px;
    color: var(--text-grey);
    white-space: nowrap;
  }

  .contact {
    position: absolute;
    font-size: 13px;
    line-height: 17.4px;
    color: var(--text-grey);
    white-space: nowrap;
  }
  .contact--address { left: 33px; top: 199px; }
  .contact--reach { top: 216px; }
  .card--row1 .contact--reach { left: 241px; }
  .card--row2 .contact--reach { left: 253px; }

  .web-tab {
    position: absolute;
    background: var(--brand-red);
    color: var(--card-white);
    display: flex;
    align-items: center;
    justify-content: center;
    white-space: nowrap;
  }
  .web-tab--side {
    right: 0;
    top: 40px;
    width: 32px;
    height: 210px;
    border-radius: 16px 0 0 16px;
  }
  .web-tab--side span {
    transform: rotate(-90deg);
    font-size: 11.5px;
  }
  .web-tab--bottom {
    left: 138px;
    top: 260px;
    width: 211px;
    height: 31px;
    border-radius: 14px 14px 0 0;
    font-size: 12px;
  }

  .slogan {
    position: absolute;
    color: var(--card-white);
    font-family: "Exo 2", sans-serif;
    font-size: 34px;
    line-height: 1;
    white-space: nowrap;
  }
  .slogan--light { font-style: italic; font-weight: 300; }
  .slogan--bold { font-weight: 600; font-size: 35px; }
</style>
</head>
<body>

  <section class="card card--front card--row1 card--left">
    <div class="brand-name">Feld und Klang</div>
    <div class="brand-tagline">GPS AUDIO APPS</div>
    <p class="contact contact--address">Lena Brandt,<br>Am Lindenhang 7,<br>78112 Musterfeld-Talheim</p>
    <p class="contact contact--reach">Tel. 49 170 0000000<br>e-mail: lena@feld-und-klang.de</p>
    <div class="web-tab web-tab--side"><span>www.feld-und-klang-beispiel.de</span></div>
  </section>

  <section class="card card--back card--row1 card--right">
    <div class="slogan slogan--light" style="left:54px; top:104px;">Orte zum</div>
    <div class="slogan slogan--light" style="left:117px; top:143px;">Sprechen bringen...</div>
  </section>

  <section class="card card--front card--row2 card--left">
    <div class="brand-name">Feld und Klang</div>
    <div class="brand-tagline">GPS AUDIO APPS</div>
    <p class="contact contact--address">Lena Brandt,<br>Am Lindenhang 7,<br>78112 Musterfeld-Talheim</p>
    <p class="contact contact--reach">Tel. 49 170 0000000<br>e-mail: lena@feld-und-klang.de</p>
    <div class="web-tab web-tab--bottom">www.feld-und-klang-beispiel.de</div>
  </section>

  <section class="card card--back card--row2 card--right">
    <div class="slogan slogan--bold" style="left:57px; top:103px;">Orte zum</div>
    <div class="slogan slogan--bold" style="left:102px; top:145px;">Sprechen bringen...</div>
  </section>

</body>
</html>
```